Business Cards for Law Office of Denise R. Harlow

I need a business card for my new estate planning law firm. I have attached my logo. I would like a design that is professional but not too formal or stuffy.

Target Market(s)

Professionals (lawyers, doctors, businesswomen) between the age of 30 and 50 who are tech-savvy and educated.

Industry/Entity Type

Lawyer

Contact Information for Business Card

Denise R. Harlow

528 E. 19th Street
7th Floor
New York, NY 10583

Phone: (855) 602-7318
Direct: (917) 463-5071
Email: Denise@DeniseRHarlowLegal.test
www.DeniseRHarlowLegal.test

Font styles to use
Other font styles liked:
• Corbel

Requirements
Must have
• On the front:
• Denise R. Harlow, Esq.
• Owner & Founder
• 528 E. 19th Street
• 7th Floor
• New York, NY 10583
• Phone: (855) 602-7318
• Direct: (917) 463-5071
• Email: denise@deniserharlowlegal.test
• www.deniserharlowlegal.test
• On the back:
• LOGO
Nice to have
• I want it to be professional but not too formal or stuffy. Please choose colors that go with my logo.
Should not have
• I don't want TOO MUCH color. Some color is good, but not too much.

```html
<!DOCTYPE html>
<html lang="en">
<head>
<meta charset="utf-8">
<title>Law Office of Denise R. Harlow — Business Cards</title>
<link href="https://fonts.googleapis.com/css2?family=Lato:wght@300;400;700&display=swap" rel="stylesheet">
<style>
  :root {
    --backdrop: #ece9e4;
    --card: #f7f7f6;
    --card-shadow: rgba(60, 50, 40, 0.18);
    --band: #dededd;
    --ink: #3a3a3a;
    --ink-soft: #6d6d6d;
    --ink-muted: #8a8a8a;
    --divider: #c9c9c9;
    --brand-purple: #7b1f7f;
  }
  * { box-sizing: border-box; margin: 0; padding: 0; }
  html, body {
    width: 1200px; height: 812px; overflow: hidden;
    background: var(--backdrop);
    font-family: "Lato", sans-serif;
  }
  .sheet {
    position: relative; width: 1200px; height: 812px;
    display: flex; align-items: center; justify-content: center; gap: 60px;
  }
  .card {
    position: relative; width: 525px; height: 300px;
    background: var(--card);
    box-shadow: 0 6px 18px var(--card-shadow);
  }
  /* Front */
  .name-band {
    position: absolute; left: 0; top: 122px; width: 255px; height: 56px;
    background: var(--band);
    padding: 10px 14px 0 22px; text-align: right;
  }
  .name-band .name {
    font-size: 15px; letter-spacing: 0.3px; color: var(--ink);
    text-transform: uppercase; white-space: nowrap; font-weight: 400;
  }
  .name-band .name strong { font-weight: 700; }
  .name-band .title {
    font-size: 10px; letter-spacing: 0.6px; color: var(--ink-muted);
    text-transform: uppercase; margin-top: 1px;
  }
  .divider {
    position: absolute; left: 272px; top: 100px; width: 1px; height: 100px;
    background: var(--divider);
  }
  .contact {
    position: absolute; left: 284px; top: 102px;
    font-size: 11.5px; line-height: 14px; color: var(--ink-soft);
    list-style: none;
  }
  .contact li { display: flex; gap: 8px; }
  .contact .icon { width: 10px; flex: none; padding-top: 2px; }
  .contact svg { width: 10px; height: 10px; fill: var(--ink-muted); }
  /* Back */
  .brand {
    position: absolute; inset: 0;
    display: flex; align-items: center; justify-content: center;
  }
  .brand-name {
    font-size: 26px; font-weight: 400; letter-spacing: 1px;
    color: var(--brand-purple); text-transform: uppercase;
  }
</style>
</head>
<body>
<main class="sheet">
  <section class="card card-front" aria-label="Front of business card">
    <div class="name-band">
      <p class="name"><strong>Denise R.</strong> Harlow, Esq.</p>
      <p class="title">Owner &amp; Founder</p>
    </div>
    <div class="divider"></div>
    <ul class="contact">
      <li><span class="icon"><svg viewBox="0 0 10 10" aria-hidden="true"><path d="M2.2 0.5 3.8 2.6 2.9 3.7C3.5 5 4.9 6.4 6.3 7.1L7.4 6.2 9.5 7.8 8.6 9.5C4.6 9.2 0.8 5.4 0.5 1.4Z"/></svg></span><span>Phone: (855) 602-7318</span></li>
      <li><span class="icon"></span><span>Direct: (917) 463-5071</span></li>
      <li><span class="icon"><svg viewBox="0 0 10 10" aria-hidden="true"><path d="M0.5 2h9v6h-9z M1 2.4 5 5.6 9 2.4" fill="none" stroke="#8a8a8a" stroke-width="1"/></svg></span><span>denise@deniserharlowlegal.test</span></li>
      <li><span class="icon"><svg viewBox="0 0 10 10" aria-hidden="true"><g fill="none" stroke="#8a8a8a" stroke-width="0.9"><circle cx="5" cy="5" r="4.2"/><ellipse cx="5" cy="5" rx="1.8" ry="4.2"/><path d="M0.8 5h8.4M1.6 2.8h6.8M1.6 7.2h6.8"/></g></svg></span><span>www.deniserharlowlegal.test</span></li>
      <li><span class="icon"><svg viewBox="0 0 10 10" aria-hidden="true"><path d="M5 0.3C3.1 0.3 1.7 1.8 1.7 3.6 1.7 6 5 9.7 5 9.7S8.3 6 8.3 3.6C8.3 1.8 6.9 0.3 5 0.3Zm0 4.6a1.2 1.2 0 1 1 0-2.4 1.2 1.2 0 0 1 0 2.4Z"/></svg></span><span>528 E. 19th Street<br>7th Floor<br>New York, NY 10583</span></li>
    </ul>
  </section>

  <section class="card card-back" aria-label="Back of business card">
    <div class="brand">
      <p class="brand-name">Law Office of Denise R. Harlow</p>
    </div>
  </section>
</main>
</body>
</html>
```